Bref créative
VELTRANO
VELTRANO Bar & Restaurant - Business Card/Stationary
I need double sided standard sized Business Card [3.5" x 2"]
Any legible font - but not boring!
Professional
Lucinda Marbella
chef de cuisine
K7 Harbor Plaza, GF/D
47th St.
Camp Valdoro
Taguig City, 1634
Manila, Philippines
veltranorestaurant@kestomail.example
facebook.example/veltranomanila, twitter.example/veltrano_

```html
<!DOCTYPE html>
<html lang="en">
<head>
<meta charset="utf-8">
<title>VELTRANO Bar &amp; Restaurant — Business Card</title>
<link rel="stylesheet" href="https://fonts.googleapis.com/css2?family=Roboto+Condensed:ital,wght@0,400;0,700;1,400&family=Open+Sans:wght@400&display=swap">
<style>
  :root {
    --stage: #e9e6e0;
    --cream: #f1e2bb;
    --cream-deep: #e6d19f;
    --paper: #ffffff;
    --ink: #1b1b1b;
    --text: #3a3a3a;
    --accent: #d98b1f;
    --shadow: rgba(0, 0, 0, 0.18);
  }
  * { box-sizing: border-box; margin: 0; padding: 0; }
  html, body { width: 1200px; height: 646px; overflow: hidden; }
  body {
    background: var(--stage);
    font-family: "Open Sans", Arial, sans-serif;
    position: relative;
  }
  .card {
    position: absolute;
    top: 175px;
    width: 520px;
    height: 297px;
    box-shadow: 0 6px 18px var(--shadow);
    overflow: hidden;
  }
  .card--front { left: 60px; }
  .card--back { left: 620px; background: var(--paper); }

  .front-pattern {
    position: absolute; inset: 0;
    background: radial-gradient(circle at 50% 50%, var(--cream) 0%, var(--cream-deep) 100%);
  }
  .wordmark {
    font-family: "Roboto Condensed", Arial, sans-serif;
    font-weight: 700;
    color: var(--ink);
    letter-spacing: 0.22em;
    white-space: nowrap;
  }
  .card--front .wordmark {
    position: absolute;
    left: 50%; top: 50%;
    transform: translate(-50%, -50%);
    font-size: 30px;
  }
  .card--back .wordmark {
    position: absolute;
    left: 46px; top: 92px;
    font-size: 24px;
  }
  .contact-owner {
    position: absolute;
    right: 30px; top: 40px;
    text-align: right;
    font-family: "Roboto Condensed", Arial, sans-serif;
  }
  .owner-name { font-weight: 700; font-size: 17px; color: var(--ink); }
  .owner-role { font-style: italic; font-size: 11px; color: var(--accent); margin-top: 1px; }
  .edge-tab {
    position: absolute;
    right: 0; top: 42px;
    width: 14px; height: 22px;
    background: var(--ink);
  }
  .address {
    position: absolute;
    left: 46px; top: 160px;
    font-size: 10.5px;
    line-height: 1.4;
    color: var(--text);
  }
  .contact-list {
    position: absolute;
    left: 46px; top: 226px;
    list-style: none;
    font-size: 10.5px;
    color: var(--text);
  }
  .contact-list li {
    display: flex; align-items: center; gap: 7px;
    height: 16px;
  }
  .contact-list svg { width: 11px; height: 11px; fill: var(--text); flex: none; }
</style>
</head>
<body>
  <section class="card card--front" aria-label="Business card front">
    <div class="front-pattern" role="img" aria-label="Cream interlocking lattice pattern"></div>
    <div class="wordmark">VELTRANO</div>
  </section>

  <section class="card card--back" aria-label="Business card back">
    <div class="wordmark">VELTRANO</div>
    <div class="contact-owner">
      <div class="owner-name">Lucinda Marbella</div>
      <div class="owner-role">chef de cuisine</div>
    </div>
    <div class="edge-tab"></div>
    <address class="address">
      K7 Harbor Plaza, GF/D 47th St.<br>
      Camp Valdoro, Taguig City,<br>
      1634, Manila, Philippines
    </address>
    <ul class="contact-list">
      <li>
        <svg viewBox="0 0 12 12" aria-hidden="true"><path d="M2.5 1h2l1 2.8-1.3 1a6 6 0 0 0 3 3l1-1.3L11 7.5v2A1.5 1.5 0 0 1 9.5 11 8.5 8.5 0 0 1 1 2.5 1.5 1.5 0 0 1 2.5 1z"/></svg>
        +63 2 555 0148
      </li>
      <li>
        <svg viewBox="0 0 12 12" aria-hidden="true"><path d="M3.5 0.5h5a1 1 0 0 1 1 1v9a1 1 0 0 1-1 1h-5a1 1 0 0 1-1-1v-9a1 1 0 0 1 1-1zm0.5 1.5v7h4v-7zm2 7.6a0.6 0.6 0 1 0 0.01 0z"/></svg>
        +63 917 555 0172
      </li>
      <li>
        <svg viewBox="0 0 12 12" aria-hidden="true"><path d="M6 0.5a5.5 5.5 0 1 0 2.7 10.3l-.5-.9A4.5 4.5 0 1 1 10.5 6v.6a1 1 0 0 1-2 0V3.5h-1v.5a2.5 2.5 0 1 0 .3 3.5 2 2 0 0 0 3.7-.9V6A5.5 5.5 0 0 0 6 .5zm0 4a1.5 1.5 0 1 1 0 3 1.5 1.5 0 0 1 0-3z"/></svg>
        veltranorestaurant@kestomail.example
      </li>
    </ul>
  </section>
</body>
</html>
```